Dr. Lumora needs a design for its website!

*Only need the design, coding is not required.
*Need desktop version ($500) and mobile/tablet version ($200)
*The attached files are not the exact layout we want, they are just for you to know what information should be included in those pages.
*The function of our website is like www.qavlo.hk
*For the background picture, prefer a lively picture and chinese people in it, NOT necessarily need a doctor or sick person in the picture

***Don't just copy the layout from the attachments or from the reference website, we are looking for creative ideas, non-ordinary designs!!!****

We are developing a website for the public to search a doctor by different criteria. At the initial stage, we need 4 pages to start with and other pages at later stage. I have attached the general idea of these pages but not necessarily to be exactly the same, I am looking for some new ideas.

This website needs a professional, modern, simple and user friendly design. The main color to be used in the website will be same as the color (R:0 G:139 B:205) used in our logo (see attached). We don't have any particular thoughts for the other color and the font to be used in the website. Can try to use circle outline for the icon in the navigation bar.

1. Home: will include 4 sections (see attached)

2. Doctor's details (see attached)

3. Health information: will include a short descriptions of this Health Info page and 5 sections (see attached)

4. News (see attached)

Reason: Not too many suitable designs to choose from and need more time to go through the designs

All

Medical

4 page

• must not be same as or looks too much like www.qavlo.hk
• prefer not to use black and red color

```html
<!DOCTYPE html>
<html lang="en">
<head>
<meta charset="utf-8">
<title>Dr. Lumora – Become a Member</title>
<link href="https://fonts.googleapis.com/css2?family=Libre+Baskerville:wght@700&family=Open+Sans:wght@400;600&display=swap" rel="stylesheet">
<style>
:root{
  --brand:#0a84c9;
  --brand-light:#4fc3f7;
  --text:#3a3a3a;
  --muted:#9a9a9a;
  --line:#d8d8d8;
  --bg:#ffffff;
  --footer-grey:#e6e6e6;
}
*{box-sizing:border-box;margin:0;padding:0}
html,body{width:867px;height:1200px;overflow:hidden;background:var(--bg)}
body{position:relative;font-family:"Open Sans",sans-serif;color:var(--text)}
.abs{position:absolute}

.utility{top:64px;right:32px;font-size:11.5px;display:flex;gap:9px;align-items:center}
.utility span+span{border-left:1px solid #555;padding-left:9px}
.utility .caret{display:inline-block;border:4px solid transparent;border-top:5px solid #333;margin:3px 5px 0 0;vertical-align:middle}

.navband{top:88px;left:0;width:867px;height:58px;background:var(--brand)}
.logo-tab{top:88px;left:64px;width:203px;height:58px;background:#fff;border-radius:22px/40px;display:flex;align-items:center;justify-content:center;gap:8px}
.logo-tab .dot{width:30px;height:30px;border-radius:50%;background:var(--brand)}
.logo-tab .name{font-size:22px;color:var(--brand);font-weight:400}
.nav a{position:absolute;top:111px;color:#fff;font-size:12px;text-decoration:none;white-space:nowrap}

.search{top:158px;left:610px;width:216px;height:26px;border:1px solid #bbb;border-radius:13px;font-size:11.5px;color:#999;padding:5px 14px}
.search svg{position:absolute;right:8px;top:5px}

.hero-photo{top:148px;left:372px;width:495px;height:480px;background:radial-gradient(ellipse at 55% 45%,#e9d2bd 0%,#e7e5e3 38%,#f3f4f5 70%,#fff 100%)}

.headline{top:200px;left:103px;font-family:"Libre Baskerville",serif;font-weight:700;color:var(--brand);font-size:36px;line-height:45px;letter-spacing:.3px}
.perks{top:298px;left:105px;list-style:none;color:var(--brand);font-size:13.5px}
.perks li{height:27.5px;display:flex;align-items:center;gap:14px}

.social-side{left:830px;width:24px;height:24px;border-radius:50%;background:var(--brand)}
.live-chat{top:425px;left:818px;width:49px;height:125px;background:var(--brand);border-radius:10px 0 0 10px;color:#fff;font-weight:600;font-size:15px}
.live-chat span{position:absolute;left:50%;top:50%;transform:translate(-50%,-50%) rotate(-90deg);white-space:nowrap}

.panel{background:#fff;border:1px solid var(--line)}
.find-form{top:455px;left:103px;width:303px;height:246px}
.login{top:546px;left:461px;width:303px;height:155px}
.label{position:absolute;font-size:12px;color:var(--text);white-space:nowrap}
.field{position:absolute;height:22px;border:1px solid #ccc;background:#fff}
.field.active{border-color:var(--brand)}
.radio{position:absolute;width:12px;height:12px;border:1px solid #aaa;border-radius:50%}
.radio.on::after{content:"";position:absolute;inset:2px;border-radius:50%;background:var(--brand)}
.btn{position:absolute;height:23px;border-radius:4px;color:#fff;font-size:12px;display:flex;align-items:center;justify-content:center;gap:8px}
.btn.primary{background:var(--brand)}
.btn.soft{background:var(--brand-light)}
.login h2{position:absolute;top:14px;width:100%;text-align:center;color:var(--brand);font-size:17px;font-weight:400}
.link{position:absolute;color:var(--brand);font-size:12px}

.result-tab{top:743px;left:0;width:160px;height:39px;border:1px solid var(--line);border-bottom:none;color:var(--brand);font-size:13px;padding:10px 29px}
.results{top:781px;left:0;width:867px}
.results .row{position:relative;height:47.5px;border-bottom:1px solid var(--line)}
.results .row.head{height:47px;background:var(--brand);border-bottom:none}
.results .cell{position:absolute;top:50%;transform:translate(-50%,-50%);white-space:nowrap;font-size:12px;color:var(--muted);line-height:1}
.results .head .cell{color:#fff;font-size:11.5px}
.c1{left:105px}.c2{left:226px}.c3{left:332px}.c4{left:439px}
.c5{left:527px}.c6{left:614px}.c7{left:697px}.c8{left:787px}

.footer h4{position:absolute;top:1042px;color:var(--brand);font-weight:400;font-size:11.5px}
.footer p{position:absolute;font-size:10.5px;line-height:13px;color:#555}
.subscribe-input{top:1072px;left:394px;width:155px;height:29px;border:1px solid #ccc;font-size:11px;color:#999;padding:6px 12px}
.subscribe-btn{top:1072px;left:557px;width:91px;height:29px;background:var(--brand);border-radius:4px;color:#fff;font-size:12.5px;display:flex;align-items:center;justify-content:center}
.foot-social{top:1077px;width:16px;height:16px;border-radius:50%;background:var(--brand)}

.legal{top:1147px;left:0;width:867px;height:27px;background:var(--footer-grey);font-size:8px;color:#666;display:flex;justify-content:center;align-items:center;gap:26px}
.legal span+span{border-left:1px solid #999;padding-left:15px;line-height:16px}
.copyright{top:1174px;left:0;width:867px;height:26px;background:var(--brand);color:#fff;font-size:8px;display:flex;align-items:center;justify-content:center}
</style>
</head>
<body>

<div class="abs utility"><span><i class="caret"></i>English</span><span>Customer Support</span><span>Call Us 852-517093</span></div>

<div class="abs navband"></div>
<div class="abs logo-tab"><span class="dot"></span><span class="name">Dr. Lumora</span></div>
<nav class="nav">
  <a style="left:385px">HOME</a>
  <a style="left:455px">DOCTOR LIST</a>
  <a style="left:546px">HEALTH INFO</a>
  <a style="left:640px">NEWS</a>
  <a style="left:697px">ABOUT US</a>
  <a style="left:769px">CONTACT US</a>
</nav>

<div class="abs hero-photo" role="img" aria-label="Photo of a smiling doctor in a white coat holding up a stethoscope"></div>

<div class="abs search">Search
  <svg width="14" height="14" viewBox="0 0 14 14"><circle cx="6" cy="6" r="4.5" fill="none" stroke="#333" stroke-width="1.5"/><line x1="9.3" y1="9.3" x2="13" y2="13" stroke="#333" stroke-width="1.5"/></svg>
</div>

<h1 class="abs headline">BECOME&nbsp; A<br>DR. LUMORA MEMBER</h1>

<ul class="abs perks">
  <li><svg width="16" height="12"><path d="M1 6l5 4 9-9" fill="none" stroke="#0a84c9" stroke-width="2"/></svg>FIRST-HAND HEALTH NEWS</li>
  <li><svg width="16" height="12"><path d="M1 6l5 4 9-9" fill="none" stroke="#0a84c9" stroke-width="2"/></svg>EXCLUSIVE PROMMOTIONS</li>
  <li><svg width="16" height="12"><path d="M1 6l5 4 9-9" fill="none" stroke="#0a84c9" stroke-width="2"/></svg>INSTANT HEALTH ADVICES</li>
  <li><svg width="16" height="12"><path d="M1 6l5 4 9-9" fill="none" stroke="#0a84c9" stroke-width="2"/></svg>FREE HEALTH SEMINARS / TALKS</li>
  <li><svg width="16" height="12"><path d="M1 6l5 4 9-9" fill="none" stroke="#0a84c9" stroke-width="2"/></svg>PRIORITY DOCTOR APPOINTMENTS</li>
</ul>

<div class="abs social-side" style="top:276px" aria-label="Social link"></div>
<div class="abs social-side" style="top:325px" aria-label="Social link"></div>
<div class="abs social-side" style="top:367px" aria-label="Social link"></div>

<div class="abs live-chat"><span>LIVE CHAT</span></div>

<form class="abs panel find-form">
  <span class="label" style="left:20px;top:22px">Doctor Name</span>
  <span class="field active" style="left:114px;top:19px;width:169px"></span>
  <span class="label" style="left:20px;top:53px">Gender</span>
  <span class="radio on" style="left:114px;top:55px"></span>
  <span class="label" style="left:141px;top:53px">Male</span>
  <span class="radio" style="left:222px;top:55px"></span>
  <span class="label" style="left:241px;top:53px">Female</span>
  <span class="label" style="left:20px;top:81px">Specialism</span>
  <span class="field" style="left:114px;top:78px;width:169px"></span>
  <span class="label" style="left:20px;top:111px">Symptoms</span>
  <span class="field" style="left:114px;top:108px;width:169px"></span>
  <span class="label" style="left:20px;top:143px">District</span>
  <span class="field" style="left:114px;top:140px;width:169px"></span>
  <span class="label" style="left:20px;top:173px">Phone Number</span>
  <span class="field" style="left:114px;top:170px;width:169px"></span>
  <span class="btn soft" style="left:114px;top:200px;width:75px">Reset</span>
  <span class="btn primary" style="left:208px;top:200px;width:75px">Search
    <svg width="12" height="12" viewBox="0 0 14 14"><circle cx="6" cy="6" r="4.5" fill="none" stroke="#fff" stroke-width="1.6"/><line x1="9.3" y1="9.3" x2="13" y2="13" stroke="#fff" stroke-width="1.6"/></svg></span>
</form>

<form class="abs panel login">
  <h2>MEMBER LOGIN</h2>
  <span class="label" style="left:19px;top:54px">Login Email</span>
  <span class="field" style="left:112px;top:50px;width:170px"></span>
  <span class="label" style="left:19px;top:84px">Password</span>
  <span class="field" style="left:112px;top:80px;width:170px"></span>
  <span class="link" style="left:111px;top:117px">Forgot Password ?</span>
  <span class="btn primary" style="left:223px;top:112px;width:59px">Login</span>
</form>

<div class="abs result-tab">SEARCH RESULT</div>
<div class="abs results" role="table">
  <div class="row head" role="row">
    <span class="cell c1">NAME</span><span class="cell c2">GENDER</span><span class="cell c3">SPECIALISM</span><span class="cell c4">SYMPTOMS</span><span class="cell c5">TYPE</span><span class="cell c6">ADDRESS</span><span class="cell c7">DISTRIC</span><span class="cell c8">PHONE NO</span>
  </div>
  <div class="row" role="row">
    <span class="cell c1">Private</span><span class="cell c2"><svg width="22" height="22" viewBox="0 0 22 22" aria-label="Doctor"><circle cx="11" cy="7" r="5" fill="#222"/><path d="M2 22c0-6 4-9 9-9s9 3 9 9z" fill="#222"/></svg></span><span class="cell c3">Private</span><span class="cell c4">Private</span><span class="cell c5">Private</span><span class="cell c6">Private</span><span class="cell c7">Private</span><span class="cell c8">Private</span>
  </div>
  <div class="row" role="row">
    <span class="cell c1">Private</span><span class="cell c2"><svg width="22" height="22" viewBox="0 0 22 22" aria-label="Doctor"><circle cx="11" cy="7" r="5" fill="#222"/><path d="M2 22c0-6 4-9 9-9s9 3 9 9z" fill="#222"/></svg></span><span class="cell c3">Private</span><span class="cell c4">Private</span><span class="cell c5">Private</span><span class="cell c6">Private</span><span class="cell c7">Private</span><span class="cell c8">Private</span>
  </div>
  <div class="row" role="row">
    <span class="cell c1">Private</span><span class="cell c2"><svg width="22" height="22" viewBox="0 0 22 22" aria-label="Doctor"><circle cx="11" cy="7" r="5" fill="#222"/><path d="M2 22c0-6 4-9 9-9s9 3 9 9z" fill="#222"/></svg></span><span class="cell c3">Private</span><span class="cell c4">Private</span><span class="cell c5">Private</span><span class="cell c6">Private</span><span class="cell c7">Private</span><span class="cell c8">Private</span>
  </div>
</div>

<footer class="footer">
  <h4 style="left:60px">DR. LUMORA.COM</h4>
  <p style="left:61px;top:1067px">About Us<br>News<br>Career<br>Partner</p>
  <h4 style="left:224px">CONTACT</h4>
  <p style="left:224px;top:1067px">help@drlumora.com<br>852-517093</p>
  <p style="left:224px;top:1106px">18 Harbour Lane Floor 3<br>Kowloon, HK 00852</p>
  <h4 style="left:393px;top:1043px">SPECIAL OFFERS</h4>
  <div class="abs subscribe-input">enter email address</div>
  <div class="abs subscribe-btn">Subscribe</div>
  <h4 style="left:698px">CONNECT WITH US</h4>
  <span class="abs foot-social" style="left:706px" aria-label="Social link"></span>
  <span class="abs foot-social" style="left:736px" aria-label="Social link"></span>
  <span class="abs foot-social" style="left:768px" aria-label="Social link"></span>
</footer>

<div class="abs legal"><span>TERM OF USE</span><span>PRIVACY POLICY</span></div>
<div class="abs copyright">Copyright 2016, DrLumora.com</div>

</body>
</html>
```